Exciting Poster Project: 4 posters for Employee Benefit Program

We are an entrepreneurial healthcare IT company that is creating an internal campaign to launch our 2017 Culture and Professional Development goals for our internal staff.

We need 4 posters utilizing the 4 campaign logos (attached) that are tied together visually into a cohesive campaign.

A PPT is included that shows the other wall art that currently exists on the walls. The new posters will share a space with these pieces.

The posters may be mounted side by side, or stand alone on a wall- so the design should work both ways. Each poster should include its own icon and the tag line provided along with topics provided that fall under this category. The posters size can be dictated by your design, but the text should be legible from a minimum of 8 feet away.

At the bottom of each poster should include all 4 icons in order to tie the entire campaign together (perhaps they can be arranged together like a diamond shape with the primary one as the biggest diamond)

Our company website for our external branding is: www.pelmaroq.com
We have included our branding guidelines for our external brand, and ppts and graphics for our internal brand.

1) Poster 1:
a. Header: Better Today Than Yesterday
b. Sub-title: Personal and Professional Growth
c. Description: We are committed to helping you build on your strengths and passions and support you your career advancement goals. We have a variety of training and development programs available to help you reach your top potential!
Leadership Development Programs
1. Supervisor Training
2. Women’s Leadership
3. Leadership Meet-Ups
4. MBA Program
Staff Development
1. Continuing Education Fund
2. Book Club
3. Pelmaroq University
4. Mentorship
5. Learning Libraries
6. Department Wide Training Events

2) Poster 2:
a. Header: Perform at Highest Capacity
b. Sub-title: Be Your Best Self
c. Description: We are committed to providing programs that bring focus to your health and overall personal wellness to encourage a well balanced life
i. Healthy Living
1. Health and wellness seminars
2. Nutrition: Fruit Delivery
ii. Fitness:
1. Step Challenge
2. Virtual 5k
3. Recess
4. Golf Lessons
5. Ping Pong Club
iii. Creativity:
1. Painting
2. Photography Club
3. Virtual Trivia
iv. Mental Health:
1. Massage Therapy
2. EAP Education
v. Financial
1. 401(k)
2. Retirement education/financial planning seminars
3. Global Insurance Program education

3) Poster 3:
a. Header: Passionate Urgent and Driven to Success
b. Sub-Header: Innovation and Strategy
c. Description: We are committed to helping you connect the dots both in the industry and with our internal goals , mission, and vision.
i. Quarterly All-Hands
ii. Lumiverse
1. Internally: Departmental and Product Updates
2. Externally: Industry Knowledge
3. Culturally: Peer to Peer Community

4) Poster 4:
a. Header: Succeed as a Team
b. Sub-Header: Cultivating Collaboration
c. Description: We are committed to creating a culture of appreciation, teamwork, and supporting an open communication. All feedback and ideas are welcome here!
i. Team Building Events
1. Employee Focused
a. Summer Picnic
b. Employee Appreciation
c. Diwali
d. Holiday Party
e. Department Appreciation
2. Family Friendly
a. Halloween
b. Bring your Kids to Work Day
3. Awards
a. Peer to Peer: QuickNod Awards
b. Leadership: Crest of Merit
4. Surveys
a. New Hire
b. Employee Engagement
Updates

Target Market(s)

Internal Employees

Industry/Entity Type

Healthcare

Font styles to use
Sans Serif

Requirements
Must have
• Job Type: Posters
• Task Outline: Create Vector Art for 4 icons and 4 posters
• Fonts and Styles to Use: SourceSansPro
Nice to have
• There is an attachment with suggested concepts and styles that we like.
Should not have
• The poster should not be very wordy or hard to read in passing.

```html
<!DOCTYPE html>
<html lang="en">
<head>
<meta charset="utf-8">
<title>Better Today Than Yesterday – Personal and Professional Growth</title>
<link href="https://fonts.googleapis.com/css2?family=Source+Sans+3:wght@300;400;600;700;900&display=swap" rel="stylesheet">
<style>
  :root {
    --teal: #1492ad;
    --crimson: #a51c30;
    --lime: #8cc63f;
    --slate: #939ea3;
    --tan: #a88a59;
    --orange: #f59f35;
    --gold: #fbb731;
    --ink: #121212;
    --white: #ffffff;
    --purple: #7b2d8e;
  }
  * { margin: 0; padding: 0; box-sizing: border-box; }
  html, body { width: 927px; height: 1200px; overflow: hidden; background: #fff; }
  body { font-family: "Source Sans 3", "Source Sans Pro", sans-serif; }

  .poster { position: relative; width: 927px; height: 1200px; overflow: hidden; background: var(--gold); }

  /* Hero */
  .hero {
    position: absolute; left: 0; top: 0; width: 927px; height: 428px;
    background: radial-gradient(ellipse at 42% 60%, #ffffff 0%, #ece7de 45%, #cfc5b6 100%);
    overflow: hidden;
  }
  .headline span {
    position: absolute; font-weight: 900; white-space: nowrap;
    letter-spacing: -0.055em; line-height: 1;
  }
  .headline .better { left: 300px; top: 10px; font-size: 118px; color: var(--teal); }
  .headline .today { left: 24px; top: 68px; font-size: 182px; color: var(--crimson); }
  .headline .than { left: 170px; top: 225px; font-size: 88px; color: var(--teal); }
  .headline .yesterday { left: 100px; top: 280px; font-size: 128px; color: var(--teal); }

  .subtitle-badge {
    position: absolute; left: 568px; top: 82px; width: 276px; height: 276px;
    background: var(--lime); border-radius: 38px; transform: rotate(45deg);
  }
  .subtitle {
    position: absolute; left: 538px; top: 166px; color: var(--white);
    font-size: 38px; font-weight: 600; line-height: 36px; letter-spacing: -0.02em;
  }

  /* Intro band */
  .intro {
    position: absolute; left: 0; top: 428px; width: 927px; height: 97px;
    background: var(--slate); color: var(--white);
    padding: 14px 20px 0 30px; font-size: 20px; font-weight: 300; line-height: 26.4px;
  }

  /* Columns */
  .column { position: absolute; top: 525px; height: 675px; background: var(--gold); }
  .column.leadership { left: 0; width: 472px; }
  .column.staff { left: 478px; width: 449px; }
  .divider { position: absolute; left: 472px; top: 525px; width: 6px; height: 675px; background: var(--white); }

  .column-title {
    position: absolute; left: 0; top: 0; width: 100%; background: var(--tan);
    color: var(--white); font-weight: 600; letter-spacing: -0.045em; white-space: nowrap;
  }
  .leadership .column-title { height: 193px; font-size: 63px; line-height: 48px; }
  .staff .column-title { height: 155px; font-size: 66px; line-height: 51px; }
  .column-title span { position: absolute; }
  .leadership .t1 { right: 12px; top: 24px; }
  .leadership .t2 { left: 26px; top: 71px; }
  .leadership .t3 { left: 124px; top: 118px; }
  .staff .t1 { right: 28px; top: 24px; }
  .staff .t2 { left: 46px; top: 75px; }

  .program {
    position: absolute; left: 0; width: 100%; color: var(--ink);
    font-size: 44px; font-weight: 400; letter-spacing: -0.055em; line-height: 44px;
    box-shadow: 0 -3px 4px rgba(0,0,0,0.12);
  }
  .program.orange { background: var(--orange); }
  .program.gold { background: var(--gold); }
  .leadership .program { padding-left: 30px; }
  .staff .program { padding-left: 46px; }

  /* Footer mark */
  .footer-mark {
    position: absolute; left: -44px; top: 992px; width: 204px; height: 204px;
    background: var(--white); border-radius: 30px; transform: rotate(45deg);
    transform-origin: center; margin-left: 0;
  }
  .footer-mark { left: -2px; top: 1034px; }
  .brand {
    position: absolute; left: 40px; top: 1080px; display: flex; align-items: center; gap: 8px;
    font-size: 26px; font-weight: 600; color: var(--purple); letter-spacing: -0.02em;
  }
  .brand .dot { width: 18px; height: 18px; background: var(--purple); border-radius: 50%; }
  .website {
    position: absolute; left: 118px; top: 1154px; font-size: 18px; font-weight: 400; color: var(--ink);
  }
</style>
</head>
<body>
<div class="poster">
  <section class="hero">
    <h1 class="headline">
      <span class="better">Better</span>
      <span class="today">Today</span>
      <span class="than">Than</span>
      <span class="yesterday">Yesterday</span>
    </h1>
    <div class="subtitle-badge"></div>
    <p class="subtitle">Personal and<br>Professional<br>Growth</p>
  </section>

  <p class="intro">We are committed to helping you build on your strengths and passions and support you your career advancement goals. We have a variety of training and development programs available to help you reach your top potential!</p>

  <section class="column leadership">
    <h2 class="column-title"><span class="t1">Leadership</span><span class="t2">Development</span><span class="t3">Programs</span></h2>
    <div class="program orange" style="top:193px;height:80px;padding-top:20px;">Supervisor Training</div>
    <div class="program gold" style="top:273px;height:64px;padding-top:9px;">Women’s Leadership</div>
    <div class="program orange" style="top:337px;height:66px;padding-top:10px;">Leadership Meet-Ups</div>
    <div class="program gold" style="top:403px;height:272px;padding-top:8px;">MBA Program</div>
  </section>

  <div class="divider"></div>

  <section class="column staff">
    <h2 class="column-title"><span class="t1">Staff</span><span class="t2">Development</span></h2>
    <div class="program gold" style="top:155px;height:106px;padding-top:8px;">Continuing<br>Education Fund</div>
    <div class="program orange" style="top:261px;height:56px;padding-top:6px;">Book Club</div>
    <div class="program gold" style="top:317px;height:106px;padding-top:8px;line-height:40px;">Pelmaroq University<br>Mentorship</div>
    <div class="program orange" style="top:423px;height:64px;padding-top:8px;">Learning Libraries</div>
    <div class="program gold" style="top:487px;height:188px;padding-top:6px;">Department Wide<br>Training Events</div>
  </section>

  <div class="footer-mark"></div>
  <div class="brand"><span class="dot"></span>Pelmaroq</div>
  <p class="website">www.pelmaroq.com</p>
</div>
</body>
</html>
```